BUSINESS CARD MIRELLE CAVANOSI

I need a new business card for my personal business.
I am a Naturopath and Nutritionist working doing private consults in the health and wellness arena.
I would like to see designs that are, clean minimalist but colourful.
I like:
White (clean,fresh, minimalist)
pops of one colour ONLY.Choose a colour to run with and keep it simple.
green
light blue
mustard
Bright yellow
Charcoal
The final design should communicate professionalism but also be in touch with nature.
Key Information to include:
MIRELLE CAVANOSI
ABN 48 217 603 915
RQTLBE 327081
Tel 0487 639 142
NATUROPATH | HERBALIST | NUTRITON CONSULTANT
BHSc (Naturopathic Studies) Grad Dip (Naturopathy)
BACK OF CARD : YOUR NEXT APPOINTMENT ..................................
I already have a logo (picture attached)But I would be more than happy to NOT have this included. I am very Open to cards WITHOUT current logo/ ones that weave the colour of my logo but do not use the logo.
I have included pictures attached to give examples of the styles/colors I enjoy.
Updates
I have added a picture of a mortar and pestle - one just like this would be lovely to include in your entry.
TIA

```html
<!DOCTYPE html>
<html lang="en">
<head>
<meta charset="utf-8">
<title>Mirelle Cavanosi Naturopathy – Business Card</title>
<link rel="stylesheet" href="https://fonts.googleapis.com/css2?family=Quicksand:wght@300;400&family=Exo+2:wght@400;600;800&display=swap">
<style>
  :root {
    --stage: #e8e3d9;
    --card: #fbfbfa;
    --accent: #f8ad3c;
    --charcoal: #2f3634;
    --charcoal-edge: #565d5b;
    --name-grey: #6f7372;
    --ink: #2a2a2a;
    --on-dark: #f2f2f2;
    --on-dark-soft: #b9bebc;
  }
  * { box-sizing: border-box; margin: 0; padding: 0; }
  html, body {
    width: 1057px; height: 1200px; overflow: hidden;
    background: var(--stage);
  }
  .sheet {
    width: 1057px; height: 1200px;
    display: grid; grid-template-rows: 600px 600px;
  }
  .panel { display: flex; align-items: center; justify-content: center; }
  .card {
    position: relative;
    width: 340px; height: 540px;
    background: var(--card);
    border: 16px solid var(--accent);
    overflow: hidden;
    box-shadow: 0 10px 26px rgba(0,0,0,0.18);
  }
  .brand { position: absolute; left: 0; right: 0; text-align: center; }
  .brand-dot {
    display: block; width: 34px; height: 34px; margin: 0 auto 12px;
    border-radius: 50%; background: var(--accent);
  }
  .brand-name {
    font-family: "Quicksand", sans-serif; font-weight: 400;
    font-size: 19px; letter-spacing: 2.5px; color: var(--name-grey);
    white-space: nowrap;
  }
  .brand-field {
    font-family: "Quicksand", sans-serif; font-weight: 400;
    font-size: 22px; letter-spacing: 5px; color: var(--accent);
    margin-top: 2px;
  }
  .card--front .brand { top: 40px; }
  .card--back .brand { top: 50%; transform: translateY(-50%); }

  .person { position: absolute; left: 24px; right: 20px; top: 186px; }
  .person-name {
    font-family: "Exo 2", sans-serif; font-weight: 800;
    font-size: 19px; letter-spacing: 0.5px; color: var(--ink);
    white-space: nowrap;
  }
  .person-role {
    font-family: "Exo 2", sans-serif; font-weight: 600;
    font-size: 9px; letter-spacing: 0.4px; color: var(--ink);
    white-space: nowrap;
  }
  .contact-band {
    position: absolute; left: 0; right: 0; top: 246px; bottom: 0;
    background: var(--charcoal);
    border-top: 5px solid var(--charcoal-edge);
    padding: 18px 24px 0;
  }
  .contact-list { list-style: none; }
  .contact-item {
    display: flex; align-items: center; gap: 12px;
    height: 28px;
    font-family: "Exo 2", sans-serif; font-size: 11px;
    letter-spacing: 0.4px; color: var(--on-dark);
    white-space: nowrap;
  }
  .contact-item--address { margin-top: 10px; }
  .contact-icon {
    width: 20px; height: 20px; flex: none;
    background: var(--on-dark); border-radius: 4px;
    display: flex; align-items: center; justify-content: center;
  }
  .contact-icon svg { width: 13px; height: 13px; }
  .credentials {
    margin-top: 16px; padding-top: 10px;
    border-top: 1px solid var(--charcoal-edge);
    font-family: "Exo 2", sans-serif; font-size: 9px;
    letter-spacing: 0.3px; line-height: 15px; color: var(--on-dark-soft);
    white-space: nowrap;
  }
  .appointment {
    position: absolute; left: 24px; right: 24px; bottom: 30px;
    font-family: "Exo 2", sans-serif; font-weight: 600;
    font-size: 9px; letter-spacing: 0.8px; color: var(--name-grey);
    white-space: nowrap; text-align: center;
  }
  .appointment-line {
    display: block; margin-top: 14px; height: 1px;
    border-bottom: 1px dotted var(--name-grey);
  }
</style>
</head>
<body>
<main class="sheet">
  <section class="panel">
    <article class="card card--front">
      <header class="brand">
        <span class="brand-dot"></span>
        <p class="brand-name">MIRELLE CAVANOSI</p>
        <p class="brand-field">NATUROPATHY</p>
      </header>
      <div class="person">
        <p class="person-name">MIRELLE CAVANOSI</p>
        <p class="person-role">NATUROPATH | HERBALIST | NUTRITION CONSULTANT</p>
      </div>
      <div class="contact-band">
        <ul class="contact-list">
          <li class="contact-item">
            <span class="contact-icon"><svg viewBox="0 0 16 16"><path fill="#2f3634" d="M4 1l2.5 3-1.4 1.6c.8 2 2.3 3.5 4.3 4.3L11 8.5l3 2.5-1.6 2.8C7 13.5 2.5 9 2.2 3.6z"/></svg></span>
            <span>Tel 0487 639 142</span>
          </li>
          <li class="contact-item">
            <span class="contact-icon"><svg viewBox="0 0 16 16"><rect x="1.5" y="3.5" width="13" height="9" fill="#2f3634"/><path d="M2 4l6 5 6-5" fill="none" stroke="#f2f2f2" stroke-width="1.2"/></svg></span>
            <span>hello@cavanosi.com</span>
          </li>
          <li class="contact-item">
            <span class="contact-icon"><svg viewBox="0 0 16 16"><g fill="none" stroke="#2f3634" stroke-width="1.4"><circle cx="8" cy="8" r="6.2"/><ellipse cx="8" cy="8" rx="2.6" ry="6.2"/><path d="M2 8h12"/></g></svg></span>
            <span>www.cavanosihealth.com</span>
          </li>
          <li class="contact-item contact-item--address">
            <span class="contact-icon"><svg viewBox="0 0 16 16"><path fill="#2f3634" d="M8 1a4.8 4.8 0 0 0-4.8 4.8C3.2 9.5 8 15 8 15s4.8-5.5 4.8-9.2A4.8 4.8 0 0 0 8 1z"/><circle cx="8" cy="5.8" r="1.8" fill="#f2f2f2"/></svg></span>
            <span>42 Fernleigh Road, Level 3 Suite 5</span>
          </li>
        </ul>
        <div class="credentials">
          <p>ABN 48 217 603 915 &nbsp;·&nbsp; RQTLBE 327081</p>
          <p>BHSc (Naturopathic Studies) Grad Dip (Naturopathy)</p>
        </div>
      </div>
    </article>
  </section>
  <section class="panel">
    <article class="card card--back">
      <header class="brand">
        <span class="brand-dot"></span>
        <p class="brand-name">MIRELLE CAVANOSI</p>
        <p class="brand-field">NATUROPATHY</p>
      </header>
      <p class="appointment">YOUR NEXT APPOINTMENT<span class="appointment-line"></span></p>
    </article>
  </section>
</main>
</body>
</html>
```